Harbin Vale Co Tank Lining Services

I would check out our website for an a quick understanding of what Blasting and Painting "is". www.harbinvaleco.example

I need to Design "sales postcard" or "company postcard" that outlines the TANK LINING division of our company. (What is a "tank lining"? It is a coating applied to the interior of a Water Tank or "Water Tower". There are certifications and special equipment needed to provide these services that make it a unique market) This is a NEW service we are offing to our customers.

We want to include photo's of: Sand Blasting, Painting, and Welding on a Ground Storage Tank. (please see attached)

Bullet points to include:
-Critical Areas
-Tank Inspections
-Manway Installation
-Fire/Domestic Water

Please Note: a little says a lot in regards to regards to data crammed into "postcards". Our market is one that won't need to be "spoon" fed. I need potential clients to read the name and our contact info (obviously).

Target Market(s)

Building Owners

Industry/Entity Type

Construction

Font styles to use
Sans Serif

Colors
0054AA
0677BA
7BADD7
CADEEF
E8F1F8

Requirements
Must have
• Layered photos or pictures
Nice to have
• Cropped Layered photos are good
Should not have
• to much clutter

```html
<!DOCTYPE html>
<html lang="en">
<head>
<meta charset="utf-8">
<title>Harbin Vale Co — Tank Lining</title>
<link rel="stylesheet" href="https://fonts.googleapis.com/css2?family=Montserrat:wght@400;500;700;800&display=swap">
<style>
  :root {
    --blue-deep: #0054AA;
    --blue-mid: #0677BA;
    --blue-bright: #0a7cc6;
    --navy: #0a2140;
    --white: #ffffff;
    --ink-soft: #f2f4f7;
  }
  html, body { margin: 0; padding: 0; overflow: hidden; background: var(--white); }
  .postcard {
    position: relative;
    width: 1200px;
    height: 655px;
    overflow: hidden;
    background: radial-gradient(circle at 48% 45%, var(--blue-bright) 0%, var(--blue-mid) 45%, var(--blue-deep) 100%);
    font-family: "Montserrat", sans-serif;
    color: var(--white);
  }
  .artwork { position: absolute; inset: 0; }
  .headline {
    position: absolute;
    right: 80px;
    top: 44px;
    margin: 0;
    text-align: right;
    line-height: 1;
    font-weight: 400;
  }
  .headline-main {
    display: block;
    font-size: 118px;
    font-weight: 800;
    letter-spacing: 0;
  }
  .headline-sub {
    display: block;
    margin-top: 0;
    font-size: 66px;
    font-weight: 500;
    letter-spacing: -1px;
  }
  .service-list {
    position: absolute;
    right: 84px;
    top: 252px;
    margin: 0;
    padding: 0;
    list-style: none;
    text-align: right;
  }
  .service-list li {
    font-size: 22px;
    font-weight: 400;
    letter-spacing: 0.6px;
    height: 45.5px;
    line-height: 30px;
  }
  .service-list li::after {
    content: "";
    display: inline-block;
    margin-left: 22px;
    width: 0; height: 0;
    border-top: 9px solid transparent;
    border-bottom: 9px solid transparent;
    border-right: 16px solid var(--white);
    vertical-align: -2px;
  }
  .contact {
    position: absolute;
    right: 148px;
    top: 538px;
    text-align: right;
  }
  .contact-label {
    display: block;
    font-size: 15px;
    font-weight: 500;
    letter-spacing: 0.3px;
  }
  .contact-phone {
    display: block;
    margin-top: 2px;
    font-size: 38px;
    font-weight: 700;
    letter-spacing: 1px;
    color: var(--ink-soft);
  }
  .brand {
    position: absolute;
    left: 43px;
    top: 582px;
    display: flex;
    align-items: center;
    gap: 12px;
  }
  .brand-mark {
    width: 36px;
    height: 36px;
    border: 3px solid var(--white);
    box-sizing: border-box;
  }
  .brand-name {
    font-size: 26px;
    font-weight: 700;
    color: var(--white);
  }
</style>
</head>
<body>
<div class="postcard">
  <svg class="artwork" width="1200" height="655" viewBox="0 0 1200 655">
    <!-- navy corner band -->
    <polygon points="0,47 600,655 0,655" fill="var(--navy)"/>

    <!-- headline lead dots -->
    <g fill="#fff">
      <circle cx="821" cy="211" r="3.5"/><circle cx="847" cy="211" r="3.5"/><circle cx="873" cy="211" r="3.5"/>
    </g>

    <!-- accent triangle -->
    <polygon points="741,480 728,502 754,502" fill="var(--navy)"/>

    <defs>
      <linearGradient id="fill-spray" x1="0" y1="0" x2="1" y2="1">
        <stop offset="0" stop-color="#d9dadc"/><stop offset="1" stop-color="#4a4643"/>
      </linearGradient>
      <linearGradient id="fill-weld" x1="0" y1="0" x2="1" y2="1">
        <stop offset="0" stop-color="#e0404e"/><stop offset="1" stop-color="#b5222e"/>
      </linearGradient>
      <linearGradient id="fill-inspect" x1="0" y1="0" x2="1" y2="1">
        <stop offset="0" stop-color="#9c9c98"/><stop offset="1" stop-color="#5a5752"/>
      </linearGradient>
    </defs>

    <!-- photo diamonds -->
    <g class="photo-frame" transform="translate(345 178) rotate(45)">
      <rect x="-117" y="-117" width="234" height="234" rx="26" fill="#fff"/>
      <rect x="-108" y="-108" width="216" height="216" rx="20" fill="url(#fill-spray)" role="img" aria-label="Photo: worker in white protective suit spray-coating the interior wall of a storage tank"/>
    </g>
    <g class="photo-frame" transform="translate(151 382) rotate(45)">
      <rect x="-114" y="-114" width="228" height="228" rx="26" fill="#fff"/>
      <rect x="-105" y="-105" width="210" height="210" rx="20" fill="url(#fill-weld)" role="img" aria-label="Photo: welder cutting steel inside a red-primed tank with sparks flying"/>
    </g>
    <g class="photo-frame" transform="translate(451 470) rotate(45)">
      <rect x="-117" y="-117" width="234" height="234" rx="26" fill="#fff"/>
      <rect x="-108" y="-108" width="216" height="216" rx="20" fill="url(#fill-inspect)" role="img" aria-label="Photo: inspector with a flashlight checking a newly lined tank interior"/>
    </g>

    <!-- phone icon -->
    <g class="phone-icon" transform="translate(1122 548) scale(-1.85 1.85)">
      <path d="M22 16.92v3a2 2 0 0 1-2.18 2 19.79 19.79 0 0 1-8.63-3.07 19.5 19.5 0 0 1-6-6 19.79 19.79 0 0 1-3.07-8.67A2 2 0 0 1 4.11 2h3a2 2 0 0 1 2 1.72 12.84 12.84 0 0 0 .7 2.81 2 2 0 0 1-.45 2.11L8.09 9.91a16 16 0 0 0 6 6l1.27-1.27a2 2 0 0 1 2.11-.45 12.84 12.84 0 0 0 2.81.7A2 2 0 0 1 22 16.92z" fill="none" stroke="#fff" stroke-width="1.3" stroke-linejoin="round" stroke-linecap="round"/>
    </g>
  </svg>

  <h1 class="headline">
    <span class="headline-main">TANK</span>
    <span class="headline-sub">LINING</span>
  </h1>

  <ul class="service-list">
    <li>Critical Areas</li>
    <li>Tank Inspections</li>
    <li>Manway Installation</li>
    <li>Fire/Domestic Water</li>
  </ul>

  <div class="contact">
    <span class="contact-label">CALL US TODAY</span>
    <span class="contact-phone">555-014-2271</span>
  </div>

  <div class="brand">
    <span class="brand-mark"></span>
    <span class="brand-name">Harbin Vale Co</span>
  </div>
</div>
</body>
</html>
```